Bref créative
Sign made using existing Logo
Sign for Valdstein Custom Homes
Needing a sign made using our existing logo.
Our logo says Valdstein
( Building Modern Luxury) but will need to say Valdstein
Custom Homes in the Same Font instead.
(sign will need to be blown up to 4ft X6ft to go in a yard) The sign will sit vertically Our logo is attached.
My vision is to have an all black sign with Logo on the left and some type of house grid or outline of a house on the right ( maybe in grey or white.)
I picture a thin grey bar going across the entire sign near the bottom that has our tag line - Building Luxury On Your Lot. and Underneath this bar ( on the black), I would like our web addresss, telephone# and Renovations to appear
www.valdcrestworks.example 555. 319.4476
It needs to say Custom Homes instead of Building Modern Luxury (Same font)

```html
<!DOCTYPE html>
<html lang="en">
<head>
<meta charset="utf-8">
<title>Valdstein Custom Homes – Yard Sign</title>
<link rel="stylesheet" href="https://fonts.googleapis.com/css2?family=Arimo:wght@700&family=Jost:wght@400;500&display=swap">
<style>
  :root {
    --page-bg: #ecedee;
    --sign-black: #000000;
    --brand-green: #8dc63f;
    --band-grey-light: #b4b6b8;
    --band-grey-dark: #8c8f91;
    --text-white: #ffffff;
    --render-grey: #4a4d50;
    --render-dark: #0c0c0c;
  }
  * { box-sizing: border-box; margin: 0; padding: 0; }
  html, body {
    width: 1200px;
    height: 901px;
    overflow: hidden;
    background: var(--page-bg);
  }
  .sign {
    position: absolute;
    left: 40px;
    top: 96px;
    width: 1120px;
    height: 708px;
    background: var(--sign-black);
    overflow: hidden;
  }
  .sign-art {
    position: absolute;
    inset: 0;
    width: 1120px;
    height: 708px;
  }
  .brand {
    position: absolute;
    left: 28px;
    top: 150px;
    width: 470px;
    display: flex;
    flex-direction: column;
    align-items: center;
  }
  .brand-dot {
    width: 150px;
    height: 150px;
    border-radius: 50%;
    border: 10px solid var(--brand-green);
    margin-bottom: 38px;
  }
  .brand-name {
    font-family: "Jost", sans-serif;
    font-weight: 400;
    font-size: 70px;
    line-height: 1;
    letter-spacing: 1px;
    color: var(--text-white);
  }
  .tagline-band {
    position: absolute;
    left: 6px;
    right: 12px;
    top: 574px;
    height: 50px;
    background: linear-gradient(180deg, var(--band-grey-light), var(--band-grey-dark));
    display: flex;
    align-items: center;
    justify-content: center;
  }
  .tagline {
    font-family: "Jost", sans-serif;
    font-weight: 500;
    font-size: 33px;
    letter-spacing: 6.5px;
    color: var(--brand-green);
    white-space: nowrap;
  }
  .contact {
    position: absolute;
    left: 34px;
    right: 22px;
    top: 640px;
    display: flex;
    justify-content: space-between;
    align-items: baseline;
    font-family: "Arimo", sans-serif;
    font-weight: 700;
    font-size: 34px;
    color: var(--text-white);
    white-space: nowrap;
  }
  .call-label { color: var(--brand-green); margin-right: 12px; }
</style>
</head>
<body>
  <div class="sign">
    <svg class="sign-art" viewBox="0 0 1120 708" xmlns="http://www.w3.org/2000/svg">
      <defs>
        <linearGradient id="render-fill" x1="0" y1="0" x2="1" y2="1">
          <stop offset="0" stop-color="var(--render-dark)"/>
          <stop offset="0.45" stop-color="var(--render-grey)"/>
          <stop offset="1" stop-color="var(--render-dark)"/>
        </linearGradient>
      </defs>
      <path class="house-render" role="img" aria-label="Wireframe architectural rendering of a custom two-storey house"
            fill="url(#render-fill)"
            d="M545 0 L1120 0 L1120 574 L575 574 C500 450 470 150 545 0 Z"/>
      <path class="divider-arc" fill="none" stroke="var(--brand-green)" stroke-width="7"
            d="M548 0 C472 150 498 450 578 574"/>
    </svg>

    <div class="brand">
      <div class="brand-dot"></div>
      <div class="brand-name">VALDSTEIN</div>
    </div>

    <div class="tagline-band">
      <span class="tagline">CUSTOM HOMES AND RENOVATIONS</span>
    </div>

    <div class="contact">
      <span class="web">www.valdcrestworks.example</span>
      <span class="phone"><span class="call-label">Call Now</span>555.319.4476</span>
    </div>
  </div>
</body>
</html>
```